Vantoralis 'Private Prism' Book Cover Design project

I need to revise the book cover design I have for my coming book. The design I created through CraftHerd is great but the book has grown and changed so I'm looking for an alternative/option design. I can then choose later from the different options.

I need a book cover that represents the unique book I am creating.

Book Title:
Your True Spectrum

Subtitle: Walking Your Path and Not Your Tag

The book is targeting all readers with a special focus on same sex attracted readers. It should not have stereotypical images.

I am including a file of the book cover I have had designed. The back cover blurb, author info and author pic will remain the same. The colouring of the back cover and spine will, of course, change to match the colouring of the front cover.

The new title will be on the spine and the new title wording.

The front cover will be markedly different using the bold images and rainbow colours of the images found in the files I am uploading for you.

I am thinking of a large boldly coloured rainbow face with the title and subtitle ON the image. The image will be the whole cover. It will fill the cover as much as possible with the text added onto the pic.

The bold pictures I am including will give you the idea of what I'm looking for.

ANY of the images I've uploaded can be used as the actual front cover image OR the designer might have/find some suitable image to be used. The image is to be large and bold and fill the cover. Hopefully a positive energy.
It needs to be eye-catching and striking and bold and positive.

So...the book cover sample file I've provided can keep the back cover with completely new colouring. The front cover is completely new with new image, wording and energy.

It is to be a rainbow coloured face or figure for the cover image.

I hope that is clear enough for you. I'm very happy to discuss and clarify these ideas with the designer. Looking forward to another great CraftHerd experience.

Target Market(s)

Wide audience with special focus on Same Sex Attracted individuals

Font styles to use
Script
Other font styles liked:
• Some form of handwriting font to make the book title and text appear more personal....as if handwritten by me.

Requirements
Must have
• Boldness, Quirky, Rainbow Colour, Image to fill the cover, maybe dark cover contrasting background.
Nice to have
• A well balanced back cover especially in the area where the barcode will be placed.
Should not have
• No stereotypical images

```html
<!DOCTYPE html>
<html lang="en">
<head>
<meta charset="utf-8">
<title>Your True Spectrum – Book Cover</title>
<link rel="stylesheet" href="https://fonts.googleapis.com/css2?family=Amatic+SC:wght@700&family=Oswald:wght@500;700&family=Barlow+Condensed:ital,wght@1,700&family=Crimson+Text:ital@0;1&family=Caveat+Brush&family=Kaushan+Script&display=swap">
<style>
  :root {
    --paper: #ffffff;
    --ink: #111111;
    --spine: #050505;
    --white: #ffffff;
    --tag: #2c2d2f;
    --tag-edge: #3a3b3e;
    --tag-text: #c9c9c9;
    --eyelet: #9a9a9a;
  }
  * { margin: 0; padding: 0; box-sizing: border-box; }
  html, body { width: 1200px; height: 927px; overflow: hidden; background: var(--paper); }
  .cover { position: relative; width: 1200px; height: 927px; color: var(--ink); overflow: hidden; }

  /* Back cover */
  .back { position: absolute; left: 0; top: 0; width: 573px; height: 927px; background: var(--paper); }
  .back-quote {
    position: absolute; left: 46px; top: 22px; width: 482px; text-align: center;
    font-family: "Amatic SC", cursive; font-weight: 700; font-size: 29px; line-height: 28.5px; letter-spacing: 1.2px;
  }
  .back-heading {
    position: absolute; left: 30px; top: 157px; width: 530px; text-align: center; white-space: nowrap;
    font-family: "Oswald", sans-serif; font-weight: 700; font-size: 20px; letter-spacing: 0.6px;
  }
  .back-subheading {
    position: absolute; left: 30px; top: 190px; width: 530px; text-align: center; white-space: nowrap;
    font-family: "Oswald", sans-serif; font-weight: 500; font-size: 16px; letter-spacing: -0.7px;
  }
  .blurb {
    position: absolute; left: 54px; width: 476px;
    font-family: "Crimson Text", serif; font-size: 17px; line-height: 19.4px; text-align: justify;
  }
  .blurb-1 { top: 228px; }
  .blurb-2 { top: 332px; left: 52px; width: 474px; }
  .blurb-3 { top: 555px; left: 52px; width: 474px; text-align: left; }
  .pull-quote {
    position: absolute; left: 64px; top: 470px; width: 436px; text-align: justify;
    font-family: "Barlow Condensed", sans-serif; font-style: italic; font-weight: 700;
    font-size: 14.5px; line-height: 18.2px; text-transform: uppercase; letter-spacing: 0.5px;
  }
  .author-photo {
    position: absolute; left: 38px; top: 638px; width: 166px; height: 120px;
    background: linear-gradient(135deg, #3e5a2c 0%, #6f8f45 45%, #2c3a22 100%);
  }
  .author-bio { position: absolute; left: 216px; top: 636px; width: 336px; font-family: "Crimson Text", serif; }
  .author-bio h3 { font-weight: 400; font-size: 18px; text-decoration: underline; letter-spacing: 0.3px; margin-bottom: 4px; }
  .author-bio p { font-style: italic; font-size: 16px; line-height: 19px; }
  .website { position: absolute; left: 33px; top: 762px; font-family: "Crimson Text", serif; font-size: 20px; }
  .brand-box {
    position: absolute; left: 37px; top: 808px; width: 144px; height: 86px; background: var(--spine);
    display: flex; align-items: center; justify-content: center;
    font-family: "Oswald", sans-serif; font-weight: 700; font-size: 15px; color: var(--white); letter-spacing: 0.5px;
  }
  .barcode-area { position: absolute; left: 375px; top: 798px; width: 170px; height: 104px; border: 1.5px solid var(--ink); background: var(--paper); }

  /* Spine */
  .spine { position: absolute; left: 573px; top: 0; width: 55px; height: 927px; background: var(--spine); }
  .spine-title {
    position: absolute; left: 50%; top: 98px; writing-mode: vertical-rl; white-space: nowrap;
    transform: translateX(-50%); color: var(--white);
    font-family: "Caveat Brush", cursive; font-size: 30px; line-height: 1;
  }
  .spine-author {
    position: absolute; left: 50%; top: 466px; writing-mode: vertical-rl; text-orientation: upright; white-space: nowrap;
    transform: translateX(-50%); color: var(--white);
    font-family: "Oswald", sans-serif; font-weight: 500; font-size: 20px; letter-spacing: 4.5px; line-height: 1;
  }

  /* Front cover */
  .front { position: absolute; left: 628px; top: 0; width: 572px; height: 927px; overflow: hidden; }
  .front-art {
    position: absolute; inset: 0;
    background:
      radial-gradient(ellipse at 30% 20%, #e0c040 0%, transparent 35%),
      radial-gradient(ellipse at 75% 25%, #d8501e 0%, transparent 40%),
      radial-gradient(ellipse at 25% 55%, #e6348c 0%, transparent 40%),
      radial-gradient(ellipse at 80% 65%, #7ec62e 0%, transparent 40%),
      radial-gradient(ellipse at 45% 85%, #2aa6c8 0%, transparent 35%),
      linear-gradient(160deg, #3a2214 0%, #6b2a18 50%, #1a1a10 100%);
  }
  .tag { position: absolute; left: 30px; top: 570px; overflow: visible; }
  .front-title {
    position: absolute; left: 58px; top: 478px; width: 470px; color: var(--white);
    font-family: "Caveat Brush", cursive; font-weight: 400; line-height: 0.86;
    transform: rotate(-4deg); transform-origin: left top; white-space: nowrap;
  }
  .front-title .line-1 { display: block; font-size: 76px; }
  .front-title .line-2 { display: block; font-size: 104px; margin-left: 52px; }
  .tag-subtitle {
    position: absolute; left: 168px; top: 716px; width: 340px; color: var(--tag-text);
    font-family: "Kaushan Script", cursive; font-size: 27px; line-height: 30px;
    transform: rotate(-13deg); transform-origin: left top; white-space: nowrap;
  }
  .tag-subtitle span { display: block; }
  .tag-subtitle span + span { margin-left: 130px; }
  .front-author {
    position: absolute; left: 102px; top: 846px; color: var(--white); white-space: nowrap;
    font-family: "Oswald", sans-serif; font-weight: 500; font-size: 50px; line-height: 1; letter-spacing: 15px;
  }
</style>
</head>
<body>
<div class="cover">
  <section class="back">
    <p class="back-quote">"It's important to challenge our accepted beliefs and the stories we tell ourselves, individually and as a community, if there is to be any sense of wholeness, happiness and future."</p>
    <h2 class="back-heading">YOUR RAINBOW IS MUCH MORE THAN THE FLAG YOU WAVE.</h2>
    <h3 class="back-subheading">IT IS THE UNIQUE AND INDIVIDUAL YOU BEHIND THE LAYERS, LABELS AND STORIES.</h3>
    <p class="blurb blurb-1">This first book by Colin Marsh asks each of us to consider our accepted beliefs and personal stories as we explore the possible ways to LIVE OUR LIFE AND NOT A LABEL. Doing this requires some honest inner work and a journey that will need to be passionately personal and authentically individual.</p>
    <p class="blurb blurb-2">‘Your True Spectrum’ reminds us that a beautiful, rainbow life is more than sexuality, personality or gender or having a camp, team or tribe to belong to. It is much more than any acronym, scene or lifestyle. It’s ‘an inside job’, deeply heartfelt and courageously unique. Finding and living the YOU of YOU has boldness and power and magic in it.</p>
    <p class="pull-quote">"Living a meaningful, happy existence is about being true to the whole, complex, integrated person that you are and being strong enough and aware enough and reflective enough to know yourself, love yourself and be yourself" Colin Marsh</p>
    <p class="blurb blurb-3">This simple and insightful book will help you explore ways to bravely and honestly know, love and be yourself no matter what the rest of the world might be doing or saying or expecting.</p>
    <div class="author-photo" role="img" aria-label="Author portrait photo, seated outdoors among greenery"></div>
    <div class="author-bio">
      <h3>COLIN MARSH</h3>
      <p>Personal Change Coach and Educator<br>VANTORALIS Coaching and Wellness Advocate, Activist, Writer and Support for MEN WHO DATE MEN and their Wholeness, Happiness and Human Rights.</p>
    </div>
    <p class="website">www.vantoralis.com</p>
    <div class="brand-box">VANTORALIS</div>
    <div class="barcode-area"></div>
  </section>

  <section class="spine">
    <p class="spine-title">YOUR TRUE SPECTRUM</p>
    <p class="spine-author">COLIN MARSH</p>
  </section>

  <section class="front">
    <div class="front-art" role="img" aria-label="Close-up painted face covered in bold rainbow paint, filling the whole cover"></div>
    <svg class="tag" width="510" height="280" viewBox="0 0 510 280" aria-hidden="true">
      <path d="M8 200 L60 110 L470 20 L492 230 L50 272 Z" fill="var(--tag)" stroke="var(--tag-edge)" stroke-width="2"/>
      <circle cx="82" cy="190" r="9" fill="var(--eyelet)"/>
      <circle cx="82" cy="190" r="4" fill="var(--tag)"/>
      <path d="M82 190 C55 198 25 208 -30 228" stroke="#e6e6e6" stroke-width="1.5" fill="none"/>
    </svg>
    <h1 class="front-title"><span class="line-1">YOUR TRUE</span><span class="line-2">SPECTRUM</span></h1>
    <p class="tag-subtitle"><span>Walking Your Path,</span><span>Not Your Tag</span></p>
    <p class="front-author">COLIN MARSH</p>
  </section>
</div>
</body>
</html>
```